(2) Trifold Brochures needed for automation industry

Need “Two” Trifold brochures. (files included) please see READ ME word doc attached.
1# will be for Pharmaceutical and Biotech companies. (stock photos and copy should be ALL pharma and biotech related.
#2 will be for food and beverage processing, Packaging & Distribution Center, Automotive, Chemical, Consumer Electronics, Government, Pulp & paper, Oil/Gas, Security & Detention, Water & Wastewater
Target Market(s)
automation industry - USA and Canada
Font styles to use
Serif
Requirements
Must have
- Target audience appeal. See attached Word file for ideas and details.
Nice to have
- Best looking Trifold Brochures in the industry
Should not have
- Cheap look

```html
<!DOCTYPE html>
<html lang="en">
<head>
<meta charset="utf-8">
<title>Vireo Automation – Trifold Brochure</title>
<link href="https://fonts.googleapis.com/css2?family=Poppins:wght@400;600;700&display=swap" rel="stylesheet">
<style>
  :root{
    --canvas:#ebebeb;
    --paper:#ffffff;
    --navy:#2b3390;
    --line:#2d6fd1;
    --ink:#231f20;
    --body:#5a5a5a;
  }
  *{margin:0;padding:0;box-sizing:border-box}
  html,body{width:1200px;height:1200px;overflow:hidden;background:var(--canvas)}
  body{position:relative;font-family:"Poppins",Arial,sans-serif;color:var(--ink)}
  .spread{position:absolute;left:238px;width:724px;height:526px;background:var(--paper);overflow:hidden}
  .spread--outside{top:55px}
  .spread--inside{top:619px}
  .spread svg.shapes{position:absolute;left:0;top:0;width:724px;height:526px}
  .fold{position:absolute;top:0;height:526px}
  .fold--left{left:0;width:246px;background:linear-gradient(90deg,transparent 80%,rgba(0,0,0,.06))}
  .fold--middle{left:246px;width:232px;background:linear-gradient(90deg,rgba(0,0,0,.09),transparent 22%,transparent 80%,rgba(0,0,0,.07))}
  .fold--right{left:478px;width:246px;background:linear-gradient(90deg,rgba(0,0,0,.05),transparent 12%)}
  .txt{position:absolute}
  .brand{display:flex;align-items:center;gap:6px;left:42px;top:40px;color:var(--navy);font-weight:700;font-size:14px;line-height:14px}
  .brand__dot{width:12px;height:12px;border-radius:50%;background:var(--navy)}
  .brand__name small{display:block;font-size:9px;line-height:11px;letter-spacing:.5px}
  .headline{font-weight:700;font-size:26px;line-height:30px;color:var(--ink)}
  .subhead{font-weight:700;color:var(--navy)}
  .copy{font-size:5.6px;line-height:9.5px;color:var(--body);text-transform:uppercase;letter-spacing:.3px}
  .contact{left:246px;width:232px;top:204px;text-align:center}
  .contact__title{font-weight:700;color:var(--navy);font-size:14px;letter-spacing:2px;margin-bottom:8px}
  .contact__line{font-size:10.5px;line-height:16px;letter-spacing:1px;color:var(--ink)}
  .contact__social{display:flex;justify-content:center;gap:16px;margin-top:10px}
  .contact__social span{width:16px;height:16px;border-radius:50%;background:var(--navy)}
</style>
</head>
<body>

<!-- Outside spread -->
<section class="spread spread--outside">
  <svg class="shapes" viewBox="0 0 604 438">
    <defs>
      <linearGradient id="photoPanel" x1="0" y1="0" x2="1" y2="1">
        <stop offset="0" stop-color="#c9ccd2"/><stop offset=".6" stop-color="#8d949e"/><stop offset="1" stop-color="#3f4752"/>
      </linearGradient>
      <linearGradient id="photoTech" x1="0" y1="0" x2="1" y2="1">
        <stop offset="0" stop-color="#5b7a8c"/><stop offset=".5" stop-color="#3b4b59"/><stop offset="1" stop-color="#23282f"/>
      </linearGradient>
    </defs>
    <rect x="12" y="13" width="580" height="412" fill="none" stroke="var(--navy)" stroke-width=".8"/>
    <path d="M150,0 C165,34 232,58 282,42 C312,32 332,12 336,0" fill="none" stroke="var(--line)" stroke-width=".8"/>
    <path d="M158,0 C172,28 230,52 278,38 C306,28 326,10 330,0 Z" fill="var(--navy)"/>
    <path d="M66,438 C106,400 160,392 232,386 C302,380 364,352 388,396 C396,414 392,430 392,438" fill="none" stroke="var(--line)" stroke-width=".8"/>
    <path d="M70,438 C110,405 160,397 230,392 C300,387 360,362 385,402 C393,420 390,438 390,438 Z" fill="var(--navy)"/>
    <path d="M40,265 C55,255 68,270 62,290 C58,305 50,312 38,308 C30,300 32,280 40,265Z" fill="var(--navy)"/>
    <path d="M56,298 C66,261 122,246 148,268 C170,290 164,362 142,388 C115,410 52,404 38,372 C28,344 46,318 56,298Z" fill="none" stroke="var(--line)" stroke-width=".8"/>
    <g role="img" aria-label="Photo: technician in a hard hat operating an industrial control cabinet">
      <path d="M60,300 C70,265 120,250 145,270 C165,290 160,360 140,385 C115,405 55,400 42,370 C32,345 50,320 60,300Z" fill="url(#photoPanel)"/>
    </g>
    <path d="M426,96 C468,74 564,80 579,118 C594,160 574,230 582,290 C589,334 545,350 498,344 C441,339 404,302 405,250 C406,198 396,116 426,96Z" fill="none" stroke="var(--line)" stroke-width=".8"/>
    <g role="img" aria-label="Photo: engineer in a hard hat testing wiring inside a control panel with a handheld meter">
      <path d="M430,100 C470,80 560,85 575,120 C590,160 570,230 578,290 C585,330 545,345 500,340 C445,335 410,300 410,250 C410,200 400,120 430,100Z" fill="url(#photoTech)"/>
    </g>
  </svg>
  <div class="fold fold--left"></div><div class="fold fold--middle"></div><div class="fold fold--right"></div>

  <div class="txt brand"><span class="brand__dot"></span><span class="brand__name">VIREO<small>AUTOMATION</small></span></div>
  <h1 class="txt headline" style="left:42px;top:122px">LOREM<br>IPSUM</h1>
  <p class="txt copy" style="left:42px;top:201px;width:180px">Lorem ipsum dolor sit amet, consectetur adipiscing elit, sed diam nonummy nibh euismod tincidunt ut laoreet dolore magna aliquam erat volutpat. Ut wisi enim ad.</p>
  <p class="txt copy" style="left:42px;top:256px;width:180px">Lorem ipsum dolor sit amet, consectetur adipiscing elit, sed diam nonummy nibh euismod tincidunt ut laoreet dolore magna aliquam erat volutpat.</p>

  <div class="txt contact">
    <h2 class="contact__title">CONTACT US</h2>
    <p class="contact__line">1234 567 89-1234 567 89</p>
    <p class="contact__line">WWW.LOREMIPSUM.COM</p>
    <p class="contact__line">123, LOREM COUNTRY</p>
    <div class="contact__social"><span></span><span></span><span></span></div>
  </div>

  <h2 class="txt subhead" style="left:497px;top:56px;font-size:18px;line-height:22px">LOREM<br>IPSUM</h2>
  <h3 class="txt subhead" style="left:497px;top:430px;font-size:11px;line-height:15px">LOREM IPSUM<br>DOLOR SIT AMET</h3>
  <p class="txt copy" style="left:497px;top:466px;width:180px">Lorem ipsum dolor sit amet, consectetur adipiscing elit, sed diam nonummy nibh euismod tincidunt ut laoreet.</p>
</section>

<!-- Inside spread -->
<section class="spread spread--inside">
  <svg class="shapes" viewBox="0 0 604 438">
    <defs>
      <linearGradient id="photoPlant" x1="0" y1="0" x2="1" y2="1">
        <stop offset="0" stop-color="#d6d8dc"/><stop offset=".5" stop-color="#a7acb3"/><stop offset="1" stop-color="#6d737c"/>
      </linearGradient>
      <linearGradient id="photoPortrait" x1="0" y1="0" x2="1" y2="1">
        <stop offset="0" stop-color="#8c939c"/><stop offset=".6" stop-color="#4c5562"/><stop offset="1" stop-color="#2c3340"/>
      </linearGradient>
    </defs>
    <rect x="12" y="13" width="580" height="412" fill="none" stroke="var(--navy)" stroke-width=".8"/>
    <path d="M245,30 C298,10 380,26 440,20 C522,13 590,26 589,100 C588,174 562,236 480,237 C398,239 348,245 288,230 C230,214 220,140 228,93 C232,57 236,38 245,30Z" fill="none" stroke="var(--line)" stroke-width=".8"/>
    <g role="img" aria-label="Photo: engineer reviewing large plans beside stainless steel process equipment and a ladder">
      <path d="M250,35 C300,15 380,30 440,25 C520,18 585,30 585,100 C585,170 560,230 480,232 C400,234 350,240 290,225 C235,210 225,140 232,95 C236,60 240,42 250,35Z" fill="url(#photoPlant)"/>
    </g>
    <path d="M604,150 C572,156 540,182 535,218 C530,262 558,298 604,306" fill="none" stroke="var(--line)" stroke-width=".8"/>
    <path d="M604,155 C575,160 545,185 540,220 C535,260 560,295 604,300Z" fill="var(--navy)"/>
    <path d="M160,290 C175,270 198,278 195,300 C193,320 180,335 165,330 C150,322 152,302 160,290Z" fill="var(--navy)"/>
    <path d="M46,306 C62,274 132,269 163,296 C190,322 184,398 152,422 C114,445 56,434 41,397 C30,366 36,328 46,306Z" fill="none" stroke="var(--line)" stroke-width=".8"/>
    <g role="img" aria-label="Photo: smiling technician writing notes at a workstation">
      <path d="M50,310 C65,280 130,275 160,300 C185,325 180,395 150,418 C115,440 60,430 45,395 C35,365 40,330 50,310Z" fill="url(#photoPortrait)"/>
    </g>
  </svg>
  <div class="fold fold--left"></div><div class="fold fold--middle"></div><div class="fold fold--right"></div>

  <div class="txt brand"><span class="brand__dot"></span><span class="brand__name">VIREO<small>AUTOMATION</small></span></div>
  <h1 class="txt headline" style="left:42px;top:100px">LOREM<br>IPSUM</h1>
  <h3 class="txt subhead" style="left:42px;top:176px;font-size:12px">UT WISI ENIM AD MINIM</h3>
  <p class="txt copy" style="left:42px;top:206px;width:180px">Lorem ipsum dolor sit amet, consectetur adipiscing elit, sed diam nonummy nibh euismod tincidunt ut laoreet dolore magna aliquam erat volutpat. Ut wisi enim ad minim veniam, quis nostrud exerci tation ullamcorper suscipit lobortis nisl ut aliquip ex ea commodo consequat.</p>
  <p class="txt copy" style="left:42px;top:293px;width:180px">Lorem ipsum dolor sit amet, consectetur adipiscing elit, sed diam nonummy nibh euismod tincidunt ut laoreet dolore magna aliquam erat volutpat. Ut wisi enim ad.</p>

  <h2 class="txt headline" style="left:275px;top:312px;font-size:24px;line-height:29px">UT WISI ENIM AD MINIM<br>VENIAM</h2>
  <p class="txt copy" style="left:275px;top:378px;width:180px">Lorem ipsum dolor sit amet, consectetur adipiscing elit, sed diam nonummy nibh euismod tincidunt ut laoreet dolore magna aliquam erat volutpat. Ut wisi enim ad minim veniam, quis nostrud exerci tation ullamcorper suscipit lobortis nisl ut aliquip ex ea commodo consequat.</p>
  <p class="txt copy" style="left:275px;top:460px;width:180px">Lorem ipsum dolor sit amet, consectetur adipiscing elit, sed diam nonummy nibh euismod tincidunt ut laoreet.</p>
  <p class="txt copy" style="left:506px;top:378px;width:180px">Lorem ipsum dolor sit amet, consectetur adipiscing elit, sed diam nonummy nibh euismod tincidunt ut laoreet dolore magna aliquam erat volutpat.</p>
  <p class="txt copy" style="left:506px;top:432px;width:180px">Lorem ipsum dolor sit amet, consectetur adipiscing elit, sed diam nonummy nibh euismod tincidunt ut laoreet dolore magna aliquam erat volutpat. Ut wisi enim ad minim veniam, quis nostrud exerci tation ullamcorper suscipit lobortis nisl.</p>
</section>

</body>
</html>
```